you will use Ai to Copy the website Quellabyx.com to come up with the basic frame work and it will give you the understanding of how I would like Zandoprik.com to be like. Zandoprik.com is a peer to peer rv rental site very similar to both of the other rv rental sites the difference is that are commission based 20% and above per rental and we will be one flat monthly rate and they keep all the earnings. Below is photo that will help you with the color scheme and the look and feel of the design

```html
<!DOCTYPE html>
<html lang="en">
<head>
<meta charset="utf-8">
<title>Zandoprik.com – Search RVs by state</title>
<link rel="stylesheet" href="https://fonts.googleapis.com/css2?family=Inter:wght@400;500;600;700;800&display=swap">
<style>
  :root{
    --ink:#10223a;
    --ink-soft:#4a5566;
    --muted:#b4bac3;
    --rule:#e6e9ee;
    --paper:#f6f7f9;
    --white:#ffffff;
    --amber:#fdb64a;
    --amber-text:#f5a524;
    --tick:#3fb471;
    --footer:#10223a;
    --footer-text:#a9b4c4;
    --footer-line:#24364f;
  }
  *{box-sizing:border-box;margin:0;padding:0}
  html,body{width:1141px;height:1200px;overflow:hidden}
  body{font-family:"Inter",sans-serif;background:var(--white);color:var(--ink)}
  a{color:inherit;text-decoration:none}

  .topbar{height:29px;background:var(--white);border-bottom:1px solid #eceef1}

  .states{height:400px;background:var(--paper);padding:48px 0 0 146px}
  .states__title{font-size:28px;font-weight:800;letter-spacing:-0.8px;line-height:1.15}
  .states__lead{font-size:12px;color:var(--ink-soft);margin-top:6px}
  .states__grid{display:grid;grid-template-columns:repeat(8,96px);column-gap:12px;margin-top:25px}
  .state{height:37.4px;border-bottom:1px solid var(--rule)}
  .state__name{display:block;font-size:10px;color:#3b4554;line-height:14px}
  .state__count{display:block;font-size:8px;color:var(--muted);line-height:12px;margin-top:1px}

  .host{position:relative;height:417px;overflow:hidden;color:var(--white)}
  .host__photo{position:absolute;inset:0;
    background:
      radial-gradient(ellipse 200px 190px at 470px 400px,rgba(196,84,34,.85),rgba(120,50,26,.4) 55%,transparent 80%),
      radial-gradient(ellipse 500px 300px at 850px 120px,#0d1522,transparent 70%),
      linear-gradient(100deg,#152236 0%,#1a2433 45%,#131d2b 70%,#0b1119 100%)}
  .host__shade{position:absolute;inset:0;background:linear-gradient(90deg,rgba(12,20,32,.55),rgba(12,20,32,.15) 60%,rgba(5,8,12,.3))}
  .host__body{position:relative;padding:62px 0 0 146px}
  .host__eyebrow{font-size:8.5px;font-weight:700;letter-spacing:1.3px;color:var(--amber-text)}
  .host__title{font-size:38px;font-weight:800;letter-spacing:-1.6px;line-height:43px;margin-top:10px}
  .host__text{font-size:12px;line-height:19.6px;width:420px;margin-top:14px;color:#e6e9ee}
  .host__perks{display:grid;grid-template-columns:211px 200px;row-gap:7px;margin-top:18px;list-style:none}
  .perk{display:flex;align-items:center;gap:5px;font-size:11px;font-weight:500;line-height:16px}
  .perk svg{width:11px;height:11px;flex:none}
  .host__actions{display:flex;gap:12px;margin-top:19px}
  .btn{height:38px;border-radius:19px;display:flex;align-items:center;justify-content:center;font-weight:600}
  .btn--primary{width:165px;background:var(--amber);color:#1b2533;font-size:12px}
  .btn--ghost{width:135px;border:1px solid rgba(255,255,255,.55);font-size:10.5px;color:var(--white)}

  .footer{height:354px;background:var(--footer);padding:0 146px;position:relative}
  .footer__top{display:flex;padding-top:57px;height:298px}
  .brand{flex:none;width:256px}
  .brand__name{font-size:15px;font-weight:700;color:var(--white);letter-spacing:-0.3px;margin-top:2px}
  .brand__text{font-size:10px;line-height:16.5px;color:var(--footer-text);width:220px;margin-top:14px}
  .social{display:flex;gap:7px;margin-top:18px}
  .social__dot{width:25px;height:25px;border-radius:50%;border:1px solid var(--footer-line)}
  .apps{margin-top:18px;display:flex;flex-direction:column;gap:6px;align-items:flex-start}
  .app{height:26px;padding:0 10px;border:1px solid #33465f;border-radius:4px;display:flex;align-items:center;gap:6px;font-size:9.5px;font-weight:600;color:var(--white);background:#17293f}
  .app__mark{width:7px;height:7px;background:var(--white);border-radius:1px}
  .col{flex:none;width:156px}
  .col--company{width:155px}
  .col--renters{width:169px}
  .col--support{flex:1 1 auto;width:auto}
  .col__head{font-size:8.5px;font-weight:700;letter-spacing:1.2px;color:var(--white);margin-top:-1px}
  .col__list{list-style:none;margin-top:21px}
  .col__list li{font-size:10.5px;color:var(--footer-text);height:26px;line-height:13px;white-space:nowrap}
  .footer__bottom{border-top:1px solid var(--footer-line);display:flex;align-items:center;height:56px;font-size:9.5px;color:var(--footer-text)}
  .legal{display:flex;gap:18px;margin-left:169px}
  .lang{margin-left:auto;height:20px;width:95px;border:1px solid #33465f;border-radius:5px;display:flex;align-items:center;justify-content:center;gap:4px;font-weight:600;color:#cfd6e0;font-size:9.5px}
</style>
</head>
<body>
  <div class="topbar"></div>

  <section class="states">
    <h2 class="states__title">Search RVs by state</h2>
    <p class="states__lead">Owner-listed RVs in all 50 states.</p>
    <div class="states__grid">
      <a class="state"><span class="state__name">Alabama</span><span class="state__count">316 RVs</span></a>
      <a class="state"><span class="state__name">Alaska</span><span class="state__count">809 RVs</span></a>
      <a class="state"><span class="state__name">Arizona</span><span class="state__count">1,194 RVs</span></a>
      <a class="state"><span class="state__name">Arkansas</span><span class="state__count">1,194 RVs</span></a>
      <a class="state"><span class="state__name">California</span><span class="state__count">6,270 RVs</span></a>
      <a class="state"><span class="state__name">Colorado</span><span class="state__count">1,480 RVs</span></a>
      <a class="state"><span class="state__name">Connecticut</span><span class="state__count">363 RVs</span></a>
      <a class="state"><span class="state__name">Delaware</span><span class="state__count">363 RVs</span></a>
      <a class="state"><span class="state__name">Florida</span><span class="state__count">2,259 RVs</span></a>
      <a class="state"><span class="state__name">Georgia</span><span class="state__count">1,118 RVs</span></a>
      <a class="state"><span class="state__name">Hawaii</span><span class="state__count">12 RVs</span></a>
      <a class="state"><span class="state__name">Idaho</span><span class="state__count">404 RVs</span></a>
      <a class="state"><span class="state__name">Illinois</span><span class="state__count">869 RVs</span></a>
      <a class="state"><span class="state__name">Indiana</span><span class="state__count">980 RVs</span></a>
      <a class="state"><span class="state__name">Iowa</span><span class="state__count">580 RVs</span></a>
      <a class="state"><span class="state__name">Kansas</span><span class="state__count">213 RVs</span></a>
      <a class="state"><span class="state__name">Kentucky</span><span class="state__count">600 RVs</span></a>
      <a class="state"><span class="state__name">Louisiana</span><span class="state__count">208 RVs</span></a>
      <a class="state"><span class="state__name">Maine</span><span class="state__count">60 RVs</span></a>
      <a class="state"><span class="state__name">Maryland</span><span class="state__count">400 RVs</span></a>
      <a class="state"><span class="state__name">Massachusetts</span><span class="state__count">369 RVs</span></a>
      <a class="state"><span class="state__name">Michigan</span><span class="state__count">1,201 RVs</span></a>
      <a class="state"><span class="state__name">Minnesota</span><span class="state__count">1,201 RVs</span></a>
      <a class="state"><span class="state__name">Mississippi</span><span class="state__count">38 RVs</span></a>
      <a class="state"><span class="state__name">North Carolina</span><span class="state__count">1,120 RVs</span></a>
      <a class="state"><span class="state__name">North Dakota</span><span class="state__count">200 RVs</span></a>
      <a class="state"><span class="state__name">Ohio</span><span class="state__count">849 RVs</span></a>
      <a class="state"><span class="state__name">Oklahoma</span><span class="state__count">573 RVs</span></a>
      <a class="state"><span class="state__name">Oregon</span><span class="state__count">1,025 RVs</span></a>
      <a class="state"><span class="state__name">Pennsylvania</span><span class="state__count">1,005 RVs</span></a>
      <a class="state"><span class="state__name">Rhode Island</span><span class="state__count">201 RVs</span></a>
      <a class="state"><span class="state__name">South Carolina</span><span class="state__count">205 RVs</span></a>
      <a class="state"><span class="state__name">South Dakota</span><span class="state__count">306 RVs</span></a>
      <a class="state"><span class="state__name">Tennessee</span><span class="state__count">588 RVs</span></a>
      <a class="state"><span class="state__name">Texas</span><span class="state__count">3,500 RVs</span></a>
      <a class="state"><span class="state__name">Utah</span><span class="state__count">1,121 RVs</span></a>
      <a class="state"><span class="state__name">Vermont</span><span class="state__count">86 RVs</span></a>
      <a class="state"><span class="state__name">Virginia</span><span class="state__count">205 RVs</span></a>
      <a class="state"><span class="state__name">Washington</span><span class="state__count">1,006 RVs</span></a>
      <a class="state"><span class="state__name">Washington, DC</span><span class="state__count">66 RVs</span></a>
      <a class="state"><span class="state__name">West Virginia</span><span class="state__count">164 RVs</span></a>
      <a class="state"><span class="state__name">Wisconsin</span><span class="state__count">386 RVs</span></a>
      <a class="state"><span class="state__name">Wyoming</span><span class="state__count">92 RVs</span></a>
    </div>
  </section>

  <section class="host">
    <div class="host__photo" role="img" aria-label="Night forest campsite with a glowing orange tent among tall dark trees"></div>
    <div class="host__shade"></div>
    <div class="host__body">
      <p class="host__eyebrow">OWN AN RV?</p>
      <h2 class="host__title">List it. Earn it.<br>Keep every dollar.</h2>
      <p class="host__text">Join thousands of hosts who stopped giving away 20% of every booking. One flat monthly membership, unlimited bookings, and you keep 100% of the payout.</p>
      <ul class="host__perks">
        <li class="perk"><svg viewBox="0 0 12 12"><rect width="12" height="12" rx="2" fill="var(--tick)"/><path d="M3 6.2l2 2 4-4.4" stroke="#fff" stroke-width="1.5" fill="none"/></svg>Free listing setup</li>
        <li class="perk"><svg viewBox="0 0 12 12"><rect width="12" height="12" rx="2" fill="var(--tick)"/><path d="M3 6.2l2 2 4-4.4" stroke="#fff" stroke-width="1.5" fill="none"/></svg>You set your own rates</li>
        <li class="perk"><svg viewBox="0 0 12 12"><rect width="12" height="12" rx="2" fill="var(--tick)"/><path d="M3 6.2l2 2 4-4.4" stroke="#fff" stroke-width="1.5" fill="none"/></svg>Verified renter profiles</li>
        <li class="perk"><svg viewBox="0 0 12 12"><rect width="12" height="12" rx="2" fill="var(--tick)"/><path d="M3 6.2l2 2 4-4.4" stroke="#fff" stroke-width="1.5" fill="none"/></svg>Zero commission, always</li>
      </ul>
      <div class="host__actions">
        <a class="btn btn--primary">Become a host, free</a>
        <a class="btn btn--ghost">How hosting works</a>
      </div>
    </div>
  </section>

  <footer class="footer">
    <div class="footer__top">
      <div class="brand">
        <p class="brand__name">Zandoprik.com</p>
        <p class="brand__text">The only RV marketplace where hosts keep 100% of their earnings. One flat monthly fee. Unlimited bookings.</p>
        <div class="social">
          <a class="social__dot" aria-label="Social profile"></a>
          <a class="social__dot" aria-label="Social profile"></a>
          <a class="social__dot" aria-label="Social profile"></a>
          <a class="social__dot" aria-label="Social profile"></a>
        </div>
        <div class="apps">
          <a class="app"><span class="app__mark"></span>Appora Store</a>
          <a class="app"><span class="app__mark"></span>Gridplay</a>
        </div>
      </div>
      <div class="col col--company">
        <p class="col__head">ZANDOPRIK.COM</p>
        <ul class="col__list"><li>Our story</li><li>Careers</li><li>Press</li><li>Blog &amp; travel guides</li><li>About us</li></ul>
      </div>
      <div class="col col--renters">
        <p class="col__head">FOR RENTERS</p>
        <ul class="col__list"><li>How renting works</li><li>Group bookings</li><li>RV delivery</li><li>National park guides</li><li>One-way rentals</li><li>RV parks &amp; campgrounds</li></ul>
      </div>
      <div class="col col--hosts">
        <p class="col__head">FOR HOSTS</p>
        <ul class="col__list"><li>Become a host</li><li>Pricing &amp; plans</li><li>Host resources</li><li>RV insurance info</li><li>Host phone app</li><li>Host tablet app</li></ul>
      </div>
      <div class="col col--support">
        <p class="col__head">SUPPORT</p>
        <ul class="col__list"><li>Help center</li><li>Contact us</li><li>Give feedback</li><li>Trust &amp; safety</li></ul>
      </div>
    </div>
    <div class="footer__bottom">
      <span>© 2025 Zandoprik.com, Inc. All rights reserved.</span>
      <nav class="legal"><a>Terms</a><a>Privacy</a><a>Cookie policy</a><a>Sitemap</a></nav>
      <span class="lang"><svg width="9" height="9" viewBox="0 0 10 10"><circle cx="5" cy="5" r="4.3" fill="none" stroke="#6aa6e8"/><path d="M.7 5h8.6M5 .7c-2.4 2.6-2.4 6 0 8.6M5 .7c2.4 2.6 2.4 6 0 8.6" fill="none" stroke="#6aa6e8" stroke-width=".8"/></svg>English (USD)</span>
    </div>
  </footer>
</body>
</html>
```